Our company is called QR horizon clinical innovatiom which based in hong kong and doing bio-medical research and production

We need a Label design for our new product Silver ion Antibacterial & Antivirus Spray.
The product features are
1. Long-lasting and long-term sterilization and anti-virus adopts ionized silver and colloidal silver technology, far exceeding the sterilization effective time of similar products on the market, and can last 7 to 20 days
2. Silver ions are harmless to human health and edible, non-volatile, can contact human skin and mouth, and the effect is far more than 75% of alcohol products and healthier than alcohol products
3. Silver ion sterilization and anti-viral spray has super anti-infection and healing effects on secondary wounds
4. Mask can be used in 7 days after one spray on it
5. can kill 99.9% bacteria and 650 species of virus
our target customers are states and europe.
6, it will come with some flavour into the product , lemon, apple , peach, lavanter and variety purfumes smells ,

the label design should have elements of
our colurs combinations navy blu-orange, anti-covid19 .

here comes with the old design and products
and the competitors design

Target Market(s)

europe and united states

Industry/Entity Type

Health Care

Logo Text

QR HORIZON CLINICAL OR QR CLIN-WORKS

Colors
3277b5
f37122

Requirements
Must have
• 1. the product specifications and details must be included just like the old one.
2.nano colloidal silver ion technology is used
3. must be emphasis the product is long acting for 7days +
4. anti virus and anti bacteriel need to be seen very well
oral cleaning , on mask on shirt on everything, surface and environmnet deinfection
Nice to have
• livible attractive design that sell itself
its not medicine but work for health

```html
<!DOCTYPE html>
<html lang="en">
<head>
<meta charset="utf-8">
<title>QR CLIN-WORKS Silver Ion Antibacterial &amp; Antivirus Spray Label</title>
<link href="https://fonts.googleapis.com/css2?family=Catamaran:wght@400;700;800&family=Exo+2:wght@600&display=swap" rel="stylesheet">
<style>
  :root {
    --navy-blue: #2f6fae;
    --blue-deep: #245d98;
    --orange: #f37122;
    --orange-deep: #e05a12;
    --green: #8ed63a;
    --white: #ffffff;
    --silver-light: #eef0f2;
    --ink: #2b2f36;
    --page: #f5f5f5;
  }
  * { box-sizing: border-box; margin: 0; padding: 0; }
  html, body { width: 839px; height: 1200px; overflow: hidden; background: var(--page); }
  body { position: relative; font-family: "Catamaran", sans-serif; }

  .label {
    position: absolute; left: 150px; top: 215px;
    width: 540px; height: 770px;
    background: var(--white);
    overflow: hidden;
    border-radius: 6px;
  }
  .label-shapes { position: absolute; inset: 0; }

  .brand { position: absolute; left: 30px; top: 36px; display: flex; align-items: center; gap: 12px; }
  .brand-dot { width: 46px; height: 46px; border-radius: 50%; background: var(--navy-blue); }
  .brand-name { font-weight: 700; font-size: 22px; color: var(--navy-blue); letter-spacing: 0.5px; }

  .claim-badge {
    position: absolute; left: 300px; top: 0; width: 130px; height: 230px;
    text-align: center; color: var(--ink);
  }
  .claim-badge svg { position: absolute; inset: 0; }
  .claim-text { position: relative; padding-top: 14px; font-weight: 800; font-size: 15px; line-height: 1.05; }
  .claim-figure { position: relative; font-weight: 800; font-style: italic; font-size: 27px; margin-top: 2px; }

  .title { position: absolute; left: 110px; top: 258px; width: 400px; text-align: center; color: var(--white); line-height: 1; }
  .title span { display: block; }
  .title-silver { font-family: "Exo 2", sans-serif; font-weight: 600; font-size: 48px; color: var(--silver-light); letter-spacing: 1px; }
  .title-main { font-weight: 800; font-size: 40px; margin-top: 6px; }
  .title-second { font-weight: 800; font-size: 40px; margin-top: 2px; }
  .title-second .accent { display: inline; color: var(--green); }
  .title-type { font-weight: 400; font-size: 30px; margin-top: 6px; padding-left: 40px; }

  .virus-art {
    position: absolute; left: 30px; top: 410px; width: 160px; height: 150px;
    border-radius: 50%;
    background: radial-gradient(circle, #9bd85a 0%, #6cb84a 45%, rgba(108,184,74,0) 72%);
  }
  .kill-claim { position: absolute; left: 220px; top: 455px; color: var(--green); font-weight: 800; font-size: 17px; line-height: 1.35; }

  .feature { position: absolute; left: 80px; display: flex; align-items: center; gap: 20px; color: var(--white); }
  .feature.long-acting { top: 535px; }
  .feature.silver-tech { top: 622px; }
  .feature-icon {
    width: 68px; height: 68px; border-radius: 50%; flex: none;
    background: var(--orange); border: 4px solid #f9a060;
    display: flex; align-items: center; justify-content: center;
  }
  .feature-head { font-weight: 800; font-size: 36px; line-height: 1; }
  .feature-body { font-weight: 700; font-size: 13px; line-height: 1.35; text-transform: uppercase; margin-top: 4px; }

  .use-row { position: absolute; left: 100px; top: 708px; display: flex; gap: 14px; list-style: none; }
  .use { width: 64px; text-align: center; color: var(--white); font-weight: 700; font-size: 8.5px; line-height: 1.15; text-transform: uppercase; }
  .use-icon { width: 30px; height: 30px; border-radius: 50%; border: 2px solid var(--white); margin: 0 auto 3px; display: block; }

  .volume {
    position: absolute; right: 0; bottom: 18px; width: 66px; height: 46px;
    background: var(--orange-deep); border-radius: 8px 0 0 8px;
    color: var(--white); font-weight: 700; font-size: 18px; white-space: nowrap;
    display: flex; align-items: center; justify-content: center;
  }
</style>
</head>
<body>
  <main class="label">
    <svg class="label-shapes" width="540" height="770" viewBox="0 0 540 770" aria-hidden="true">
      <path d="M0 150 L300 110 L300 0 L540 0 L540 770 L0 770 Z" fill="var(--orange)"/>
      <path d="M58 240 Q60 190 110 184 L540 110 L540 770 L58 770 Z" fill="var(--white)"/>
      <path d="M70 248 Q72 202 118 196 L540 124 L540 770 L70 770 Z" fill="var(--navy-blue)"/>
      <path d="M70 540 L70 770 L300 770 Z" fill="var(--blue-deep)" opacity="0.35"/>
    </svg>

    <div class="brand">
      <span class="brand-dot"></span>
      <span class="brand-name">QR CLIN-WORKS</span>
    </div>

    <div class="claim-badge">
      <svg width="130" height="230" viewBox="0 0 130 230" aria-hidden="true">
        <defs>
          <linearGradient id="silverFill" x1="0" x2="1">
            <stop offset="0" stop-color="#a9aeb4"/>
            <stop offset="0.5" stop-color="#f1f2f3"/>
            <stop offset="1" stop-color="#9aa0a6"/>
          </linearGradient>
        </defs>
        <path d="M0 0 H130 V160 A65 65 0 0 1 0 160 Z" fill="#3a4a60"/>
        <path d="M6 0 H124 V158 A59 59 0 0 1 6 158 Z" fill="url(#silverFill)"/>
        <circle cx="65" cy="160" r="42" fill="none" stroke="var(--ink)" stroke-width="5"/>
        <circle cx="65" cy="160" r="16" fill="var(--ink)"/>
        <line x1="37" y1="132" x2="93" y2="188" stroke="var(--ink)" stroke-width="5"/>
      </svg>
      <p class="claim-text">KILLS VIRUS<br>&amp; BACTERIA</p>
      <p class="claim-figure">99,99%</p>
    </div>

    <h1 class="title">
      <span class="title-silver">SILVER ION</span>
      <span class="title-main">ANTIBACTERIAL</span>
      <span class="title-second">&amp; <span class="accent">ANTIVIRUS</span></span>
      <span class="title-type">SPRAY</span>
    </h1>

    <div class="virus-art" role="img" aria-label="Green virus particle dissolving into fragments"></div>
    <p class="kill-claim">CAN KILL 99.9% BACTERIA<br>AND 650 SPECIES OF VIRUS</p>

    <section class="feature long-acting">
      <div class="feature-icon">
        <svg width="30" height="30" viewBox="0 0 30 30" aria-hidden="true">
          <rect x="3" y="5" width="24" height="22" rx="3" fill="none" stroke="#fff" stroke-width="2.5"/>
          <line x1="3" y1="11" x2="27" y2="11" stroke="#fff" stroke-width="2.5"/>
          <text x="15" y="24" text-anchor="middle" font-family="Catamaran, sans-serif" font-weight="800" font-size="12" fill="#fff">7</text>
        </svg>
      </div>
      <div>
        <p class="feature-head">7DAYS +</p>
        <p class="feature-body">Must be emphasis the product<br>is long acting</p>
      </div>
    </section>

    <section class="feature silver-tech">
      <div class="feature-icon">
        <svg width="30" height="30" viewBox="0 0 30 30" aria-hidden="true">
          <circle cx="15" cy="15" r="6" fill="none" stroke="#fff" stroke-width="2.5"/>
          <circle cx="15" cy="4" r="2.5" fill="#fff"/><circle cx="15" cy="26" r="2.5" fill="#fff"/>
          <circle cx="5" cy="9" r="2.5" fill="#fff"/><circle cx="25" cy="9" r="2.5" fill="#fff"/>
          <circle cx="5" cy="21" r="2.5" fill="#fff"/><circle cx="25" cy="21" r="2.5" fill="#fff"/>
        </svg>
      </div>
      <div>
        <p class="feature-head">SILVER ION</p>
        <p class="feature-body">Nano colloidal silver ion<br>technology is used</p>
      </div>
    </section>

    <ul class="use-row">
      <li class="use"><span class="use-icon"></span>Hand<br>protection</li>
      <li class="use"><span class="use-icon"></span>Face mask<br>surface</li>
      <li class="use"><span class="use-icon"></span>Oral<br>cleaning</li>
      <li class="use"><span class="use-icon"></span>Maternal and<br>child safety</li>
    </ul>

    <div class="volume">100 ML</div>
  </main>
</body>
</html>
```